Brindle Cyto company values interaction - arch and foundation

We need a graphic that represents the relationship between our company's values. Our company, Brindle Cyto, is a biotechnology startup based in Seattle. We are pushing the boundaries of biology to create tailored cell therapy solutions through protein design and custom programming to cure diseases. Our values are Respect, Inclusion, Science, Innovation and Collaboration. We view Respect and Inclusion as the foundation on which our other values rest, with Science and Collaboration supporting Innovation. We have styled this as an arch with Innovation in the middle (see attached file). We would like to show this graphic on our careers page to help candidates know what we're all about. See: https://www.brindlecyto.example/careers

Target Market(s)

Potential job applicants, current employees and anyone who wants to know what we're about

Industry/Entity Type

Biotechnology

Font styles to use
Sans Serif

Colors

Designer to choose colors to be used in the design.

Requirements
Must have
• A foundation that supports an arch to demonstrate how our values drive our culture and mission

```html
<!DOCTYPE html>
<html lang="en">
<head>
<meta charset="utf-8">
<title>Brindle Cyto – Our Values</title>
<link rel="stylesheet" href="https://fonts.googleapis.com/css2?family=Source+Sans+3:wght@600;700&display=swap">
<style>
  :root {
    --page-bg: #ffffff;
    --arch-light: #62cfd8;
    --arch-light-edge: #3fb3bd;
    --brand-blue: #0e66a8;
    --brand-blue-edge: #0a4f86;
    --label: #ffffff;
    --label-shadow: rgba(0, 30, 60, 0.75);
  }
  html, body {
    margin: 0;
    padding: 0;
    width: 1200px;
    height: 675px;
    overflow: hidden;
    background: var(--page-bg);
  }
  .values-graphic {
    display: block;
    width: 1200px;
    height: 675px;
  }
  .value-label {
    font-family: "Source Sans 3", "Source Sans Pro", sans-serif;
    font-weight: 700;
    font-variant: small-caps;
    fill: var(--label);
    filter: url(#label-shadow);
  }
  .value-label--arch { font-size: 27px; letter-spacing: 0; }
  .value-label--base { font-size: 48px; letter-spacing: 0; }
  .arch-side { fill: var(--arch-light); stroke: var(--arch-light-edge); stroke-width: 1.5; }
  .arch-keystone { fill: var(--brand-blue); stroke: var(--brand-blue-edge); stroke-width: 1.5; }
  .foundation-block { fill: var(--brand-blue); stroke: var(--brand-blue-edge); stroke-width: 1.5; }
  .arch-gap { stroke: var(--page-bg); stroke-width: 12; }
</style>
</head>
<body>
<svg class="values-graphic" viewBox="0 0 1200 675" role="img" aria-label="Brindle Cyto values: Science, Innovation and Collaboration form an arch resting on a foundation of Respect and Inclusion">
  <defs>
    <filter id="label-shadow" x="-10%" y="-30%" width="120%" height="160%">
      <feDropShadow dx="1.5" dy="1.5" stdDeviation="1" flood-color="var(--label-shadow)"/>
    </filter>
    <filter id="block-shadow" x="-5%" y="-5%" width="110%" height="110%">
      <feDropShadow dx="0" dy="1" stdDeviation="1.2" flood-color="rgba(0,40,70,0.35)"/>
    </filter>
    <path id="arch-text-path" d="M338,467.5 A262,262 0 0 1 862,467.5"/>
  </defs>

  <!-- Arch -->
  <g class="arch" filter="url(#block-shadow)">
    <path class="arch-side" d="M294,361 A324,324 0 0 1 906,361 L789,361 A217,217 0 0 0 411,361 Z"/>
    <path class="arch-keystone" d="M489.2,163 A324,324 0 0 1 710.8,163 L674.2,263.6 A217,217 0 0 0 525.8,263.6 Z"/>
  </g>
  <line class="arch-gap" x1="531.6" y1="279.5" x2="477" y2="129.5"/>
  <line class="arch-gap" x1="668.4" y1="279.5" x2="723" y2="129.5"/>

  <text class="value-label value-label--arch" text-anchor="middle">
    <textPath href="#arch-text-path" startOffset="24%">Science</textPath>
  </text>
  <text class="value-label value-label--arch" text-anchor="middle">
    <textPath href="#arch-text-path" startOffset="50%">Innovation</textPath>
  </text>
  <text class="value-label value-label--arch" text-anchor="middle">
    <textPath href="#arch-text-path" startOffset="74.8%">Collaboration</textPath>
  </text>

  <!-- Foundation -->
  <g class="foundation" filter="url(#block-shadow)">
    <rect class="foundation-block" x="292.5" y="375" width="301.5" height="97.5"/>
    <rect class="foundation-block" x="606" y="375" width="301" height="97.5"/>
  </g>
  <text class="value-label value-label--base" x="446" y="441" text-anchor="middle" textLength="146" lengthAdjust="spacingAndGlyphs">Respect</text>
  <text class="value-label value-label--base" x="757" y="441" text-anchor="middle" textLength="182" lengthAdjust="spacingAndGlyphs">Inclusion</text>
</svg>
</body>
</html>
```